eCommerce Landing Page Design for Wine Accessories using PageFly

Need to develop a landing page template that can be used for ecommerce products. This template needs to be built in PageFly (shopify App) if not in Pagefly, need an integrated app with shopify to maintain the correct url. The website is www.bluemarrowden.com. The template will be built using one product as an example. Copy and product images will be provided. the Landing page also must have "15% Off" and "free shipping" somewhere on the page

Although part of a website, I am open to different options on design

Target Market(s)

Wine drinkers

Requirements
Must have
• Built in PageFly (shopify App)
• Featured Product
• 15% Off
• Free Shipping
• High Converting with add to cart actions directly on the page

```html
<!DOCTYPE html>
<html lang="en">
<head>
<meta charset="utf-8">
<title>Blue Marrowden – Wine Accessories</title>
<link href="https://fonts.googleapis.com/css2?family=Oswald:wght@300;400;500;600;700&display=swap" rel="stylesheet">
<style>
  :root{
    --brand-red:#b80a2f;
    --wine-red:#c30d35;
    --ink:#111111;
    --text:#4a4a4a;
    --muted:#8a8a8a;
    --rule:#d6d6d6;
    --section-grey:#f0f0f0;
    --rating-green:#1fb24a;
    --offer-green:#22a33a;
    --cart-yellow:#ffb400;
    --white:#ffffff;
  }
  *{box-sizing:border-box;margin:0;padding:0}
  html,body{width:1024px;height:1200px;overflow:hidden;background:var(--white)}
  body{font-family:"Oswald",sans-serif;color:var(--text);position:relative}

  /* header */
  .site-header{position:absolute;left:0;top:0;width:1024px;height:132px;border-bottom:1px solid var(--rule)}
  .contact{position:absolute;left:116px;top:51px;font-size:14.5px;font-weight:300;line-height:21px;text-align:right;color:var(--text)}
  .icon-ring{position:absolute;width:30px;height:30px;border:1px solid #cfcfcf;border-radius:50%;display:flex;align-items:center;justify-content:center}
  .icon-phone{left:269px;top:56px}
  .icon-cart{left:724px;top:56px}
  .brand-name{position:absolute;left:0;width:1024px;top:52px;text-align:center;font-size:30px;font-weight:500;color:var(--brand-red);letter-spacing:.5px}
  .cart-summary{position:absolute;left:771px;top:51px;font-size:14.5px;font-weight:300;line-height:21px;color:#333}

  .main-nav{position:absolute;top:132px;left:0;width:1024px;height:60px}
  .main-nav a{position:absolute;top:13px;font-size:19px;font-weight:300;color:#444;text-decoration:none}

  /* hero */
  .hero{position:absolute;top:192px;left:0;width:1024px;height:383px;background:#000;overflow:hidden}
  .hero-photo-left{position:absolute;left:0;top:0;width:460px;height:383px;
    background:radial-gradient(ellipse at 60% 90%,#8a1234 0%,#3a0616 40%,transparent 70%),
               radial-gradient(ellipse at 20% 60%,#9a9a9a 0%,#4a4a4a 25%,transparent 50%),
               radial-gradient(ellipse at 72% 40%,#d8d8d8 0%,#5a5a5a 18%,transparent 38%)}
  .hero-photo-right{position:absolute;right:0;top:0;width:300px;height:383px;
    background:radial-gradient(ellipse at 100% 85%,#ff9a1a 0%,#c43d06 25%,transparent 55%),
               radial-gradient(ellipse at 40% 75%,#a3001c 0%,#4a0010 35%,transparent 60%),
               radial-gradient(ellipse at 85% 10%,#7a0a18 0%,#2a0006 30%,transparent 55%)}
  .hero-title{position:absolute;left:387px;top:84px;font-size:28.5px;font-weight:700;line-height:1.2;color:var(--white);letter-spacing:.3px;text-transform:uppercase;white-space:nowrap}
  .hero-copy{position:absolute;left:391px;top:137px;width:400px;font-size:13.6px;font-weight:600;line-height:17.5px;color:var(--white)}
  .hero-cta{position:absolute;left:570px;top:245px;width:140px;height:52px;background:var(--wine-red);color:var(--white);font-size:15px;font-weight:600;display:flex;align-items:center;justify-content:center}
  .hero-arrow{position:absolute}
  .arrow-prev{left:86px;top:156px}
  .arrow-next{left:911px;top:158px}
  .hero-dots{position:absolute;top:356px;left:494px;display:flex;gap:4px}
  .hero-dots span{width:9px;height:9px;border-radius:50%;background:#bbb}
  .hero-dots span:first-child{background:#fff}

  /* promos */
  .promo{position:absolute;top:603px;height:188px;background:var(--ink);color:var(--white);overflow:hidden}
  .promo-discount{left:111px;width:386px}
  .promo-shipping{left:528px;width:384px}
  .promo-photo{position:absolute;top:0;height:188px}
  .promo-discount .promo-photo{left:0;width:189px;background:linear-gradient(160deg,#f3ece6 0%,#e9d6c4 55%,#caa37b 100%)}
  .promo-shipping .promo-photo{right:0;width:180px;background:linear-gradient(160deg,#f4efe8 0%,#ece0d2 55%,#d7b794 100%)}
  .big-number{position:absolute;left:208px;top:25px;font-size:58px;font-weight:500;line-height:1}
  .big-number small{font-size:28px;font-weight:600}
  .promo-sub{position:absolute;left:257px;top:88px;font-size:17px;font-weight:300}
  .promo-head{position:absolute;left:43px;top:30px;font-size:21px;font-weight:600}
  .promo-body{position:absolute;left:43px;top:66px;width:140px;font-size:11px;font-weight:500;line-height:13.5px}
  .promo-btn{position:absolute;top:146px;width:73px;height:27px;background:var(--wine-red);color:var(--white);font-size:11px;font-weight:600;display:flex;align-items:center;justify-content:center}
  .promo-discount .promo-btn{left:252px}
  .promo-shipping .promo-btn{left:43px}

  /* products */
  .products{position:absolute;top:832px;left:0;width:1024px;height:368px;background:var(--section-grey)}
  .section-title{position:absolute;left:0;width:1024px;top:0;text-align:center;font-size:30px;font-weight:700;color:#444;letter-spacing:.5px}
  .product-card{position:absolute;top:45px;width:256px;height:308px;background:var(--white);border:1px solid #dcdcdc}
  .product-photo{height:155px;border-bottom:1px solid #e4e4e4}
  .product-name{position:absolute;left:18px;top:168px;font-size:17px;font-weight:500;color:#444;letter-spacing:.2px}
  .rating{position:absolute;left:29px;top:195px;width:48px;height:19px;background:var(--rating-green);color:var(--white);font-size:11.5px;font-weight:500;display:flex;align-items:center;padding-left:4px;gap:2px}
  .rating small{font-size:5px}
  .price{position:absolute;left:155px;top:198px;font-size:11.5px;color:#333}
  .price-old{position:absolute;left:205px;top:198px;font-size:11.5px;color:var(--muted);text-decoration:line-through}
  .offer{position:absolute;left:26px;top:230px;font-size:11px;color:#333}
  .offer .tag{color:var(--offer-green)}
  .offer .pct{color:var(--wine-red);margin-left:6px}
  .btn{position:absolute;top:257px;width:112px;height:39px;color:var(--white);font-size:17px;font-weight:500;display:flex;align-items:center;justify-content:center}
  .btn-buy{left:12px;background:var(--wine-red)}
  .btn-cart{left:132px;background:var(--cart-yellow)}
</style>
</head>
<body>

<header class="site-header">
  <div class="contact">CALL US: 123-456-7890<br>hello@bluemarrowden.com</div>
  <div class="icon-ring icon-phone">
    <svg width="14" height="14" viewBox="0 0 24 24" fill="none" stroke="#aaa" stroke-width="1.6"><path d="M5 3h4l2 5-2.5 1.5a11 11 0 0 0 6 6L16 13l5 2v4a2 2 0 0 1-2 2A16 16 0 0 1 3 5a2 2 0 0 1 2-2z"/></svg>
  </div>
  <div class="brand-name">Blue Marrowden</div>
  <div class="icon-ring icon-cart">
    <svg width="15" height="15" viewBox="0 0 24 24" fill="none" stroke="#aaa" stroke-width="1.6"><path d="M2 3h3l3 12h11l2-8H6"/><circle cx="9" cy="19" r="1.6"/><circle cx="17" cy="19" r="1.6"/></svg>
  </div>
  <div class="cart-summary">YOUR CART:<br>0 items - $0.00</div>
</header>

<nav class="main-nav">
  <a href="#" style="left:268px">Home</a>
  <a href="#" style="left:396px">About</a>
  <a href="#" style="left:524px">Product</a>
  <a href="#" style="left:666px">ContactUs</a>
</nav>

<section class="hero">
  <div class="hero-photo-left" role="img" aria-label="Silver cufflinks and a crystal wine glass charm on red velvet"></div>
  <div class="hero-photo-right" role="img" aria-label="Red wine pouring from a bottle into a glass beside a fire"></div>
  <h1 class="hero-title">Beautifully Crafted Stainless</h1>
  <p class="hero-copy">STEEL WINE GLASS—Order in your favorite color or collect all 8 colors to match with any occasion or outfit. You will LOVE to use and show off your new stylish, fun, trendy, sassy and chic wine glass!</p>
  <div class="hero-cta">SHOP NOW</div>
  <svg class="hero-arrow arrow-prev" width="28" height="44" viewBox="0 0 28 44"><path d="M26 2 4 22l22 20" fill="none" stroke="#fff" stroke-width="2.5"/></svg>
  <svg class="hero-arrow arrow-next" width="28" height="44" viewBox="0 0 28 44"><path d="M2 2l22 20L2 42" fill="none" stroke="#fff" stroke-width="2.5"/></svg>
  <div class="hero-dots"><span></span><span></span><span></span></div>
</section>

<section class="promo promo-discount">
  <div class="promo-photo" role="img" aria-label="Stainless steel wine glasses in red, silver and purple on a wooden table"></div>
  <div class="big-number">15% <small>off</small></div>
  <div class="promo-sub">On All Products</div>
  <div class="promo-btn">Shop Now</div>
</section>

<section class="promo promo-shipping">
  <div class="promo-head">FREE SHIPPING</div>
  <div class="promo-body">This is the Perfect Anything Outdoors Wine Glass! Per-fect</div>
  <div class="promo-btn">Shop Now</div>
  <div class="promo-photo" role="img" aria-label="Red stainless steel wine glass on a table with flowers"></div>
</section>

<section class="products">
  <h2 class="section-title">OUR PRODUCT</h2>

  <article class="product-card" style="left:112px">
    <div class="product-photo" role="img" aria-label="Wine aerator pourer filling a glass with red wine" style="background:linear-gradient(135deg,#f7f7f7 0%,#ececec 55%,#e3c3c8 100%)"></div>
    <h3 class="product-name">Lorem Ipsum is simply dummy</h3>
    <div class="rating">4.5★ <small>(69)</small></div>
    <span class="price">$24.68</span><span class="price-old">$47.126</span>
    <p class="offer"><span class="tag">Offers</span> Special Price <span class="pct">50% off</span></p>
    <div class="btn btn-buy">Buy Now</div><div class="btn btn-cart">Add to Cart</div>
  </article>

  <article class="product-card" style="left:384px">
    <div class="product-photo" role="img" aria-label="Wine barrel and bottle canvas wall art set" style="background:radial-gradient(ellipse at 50% 55%,#8a5a2e 0%,#3b2414 45%,#d4d4d4 75%)"></div>
    <h3 class="product-name">Lorem Ipsum is simply dummy</h3>
    <div class="rating">4.5★ <small>(69)</small></div>
    <span class="price">$24.68</span><span class="price-old">$47.126</span>
    <p class="offer"><span class="tag">Offers</span> Special Price <span class="pct">50% off</span></p>
    <div class="btn btn-buy">Buy Now</div><div class="btn btn-cart">Add to Cart</div>
  </article>

  <article class="product-card" style="left:656px">
    <div class="product-photo" role="img" aria-label="Purple stainless steel wine glass with flowers behind" style="background:radial-gradient(ellipse at 50% 35%,#b42bc4 0%,#8b1f9a 25%,#efe4d8 55%)"></div>
    <h3 class="product-name">Lorem Ipsum is simply dummy</h3>
    <div class="rating">4.5★ <small>(69)</small></div>
    <span class="price">$24.68</span><span class="price-old">$47.126</span>
    <p class="offer"><span class="tag">Offers</span> Special Price <span class="pct">50% off</span></p>
    <div class="btn btn-buy">Buy Now</div><div class="btn btn-cart">Add to Cart</div>
  </article>
</section>

</body>
</html>
```